Key Scientific Research Plastics Presentation - 5 Slides

We need the attached slides reworked with the following changes:

Information needs to be very visually stunning and easily understood
Text/font treatments should attract attention
All graphs and infographics can be recreated to match style
Attached color palette is not necessary, but can be used

Please reach out with any questions.

```html
<!DOCTYPE html>
<html lang="en">
<head>
<meta charset="utf-8">
<title>Plastics Research Presentation – Five Slides</title>
<link href="https://fonts.googleapis.com/css2?family=Montserrat:wght@500;600;700&family=Questrial&display=swap" rel="stylesheet">
<style>
  :root{
    --stage:#4a4a4a;
    --olive:#9aa21a;
    --olive-light:#e1e2a8;
    --gold:#b8860b;
    --gold-warm:#c9961a;
    --gold-light:#ead9ad;
    --blue:#5d8fb0;
    --blue-light:#c7d7e3;
    --brown:#6b2e1f;
    --orange:#f0a020;
    --ink:#4a4a4a;
    --ink-soft:#6d6d6d;
    --white:#ffffff;
  }
  *{margin:0;padding:0;box-sizing:border-box}
  html,body{width:1200px;height:613px;overflow:hidden;background:var(--stage)}
  body{position:relative;font-family:"Questrial",sans-serif;color:var(--ink)}
  .slide{position:absolute;width:340px;height:256px;overflow:hidden;
    background:radial-gradient(ellipse at 70% 40%,#ffffff 0%,#f4f4f4 55%,#ebebeb 100%)}
  .abs{position:absolute}
  .band{position:absolute;left:26px;top:0;width:88px;height:230px;border-bottom-right-radius:22px}
  .header{position:absolute;left:26px;top:26px;width:288px;height:46px;border-bottom-right-radius:22px}
  .title{font-family:"Montserrat",sans-serif;font-weight:700;color:var(--white);line-height:1.15;white-space:nowrap}
  .quote{position:absolute;color:var(--white);text-align:center;font-size:6.6px;line-height:7.9px}
  .quote-mark{position:absolute;font-family:"Montserrat",sans-serif;font-weight:700;font-size:40px;line-height:1;opacity:.35;color:var(--white)}
  .brand{position:absolute;display:flex;align-items:center;gap:3px}
  .brand-dot{width:30px;height:30px;border-radius:50%;background:var(--white)}
  .brand-name{font-family:"Questrial",sans-serif;font-size:6px;line-height:6.5px;color:var(--white);width:34px}
  .small{font-size:5.9px;line-height:7.4px}
  .tiny{font-size:4.5px;line-height:5.6px;color:var(--ink-soft)}
  b{font-family:"Montserrat",sans-serif;font-weight:700}
  .lbl{font-family:"Montserrat",sans-serif;font-weight:700}

  /* slide 1 checklist */
  .check-row{position:absolute;left:132px;width:182px;border-radius:8px;display:flex;align-items:center;font-size:6.6px;line-height:7.8px}
  .check-row .ico{width:15px;height:15px;border-radius:50%;flex:none;margin:0 5px 0 0;display:flex;align-items:center;justify-content:center}
  .row-yes{background:var(--olive-light)} .row-yes .ico{background:var(--olive)}
  .row-ask{background:var(--blue-light)} .row-ask .ico{background:var(--blue)}
  .row-no{background:var(--gold-light)} .row-no .ico{background:var(--gold)}
  .ask-pill{position:absolute;left:132px;top:204px;width:176px;height:26px;border:1px solid var(--gold);border-radius:13px;
    display:flex;align-items:center;padding-left:8px;font-family:"Montserrat",sans-serif;font-weight:700;font-size:8px;color:var(--gold)}

  /* slide 4 */
  .risk-node{position:absolute;border-radius:50%;border:2px solid #fff;box-shadow:0 1px 3px rgba(0,0,0,.3);display:flex;flex-direction:column;align-items:center;justify-content:center;color:#fff;font-size:3.8px}
  .risk-box{position:absolute;left:259px;top:81px;width:55px;height:84px;background:#fff;box-shadow:0 1px 4px rgba(0,0,0,.18);font-size:5px;line-height:6.2px;text-align:center;color:var(--ink);padding-top:9px}

  /* slide 5 table */
  .table-head{position:absolute;left:26px;top:90px;width:93px;height:42px;background:var(--blue);border-radius:21px;color:#fff;font-size:5.2px;line-height:6px}
  .trow{position:absolute;left:26px;width:93px;font-size:5.3px;line-height:6.3px;color:var(--ink)}
  .trow .k{position:absolute;right:51px;text-align:right}
  .trow .v{position:absolute;left:49px}
  .trule{position:absolute;left:42px;width:68px;height:.6px;background:var(--ink-soft)}
</style>
</head>
<body>

<!-- ===== Slide 1 : Treaty checks and balances ===== -->
<section class="slide" style="left:246px;top:36px">
  <div class="band" style="background:linear-gradient(180deg,var(--olive),#8f9618)"></div>
  <div class="header" style="background:linear-gradient(90deg,var(--olive) 0%,#a99415 45%,var(--gold-warm) 100%)"></div>
  <div class="brand" style="left:42px;top:34px"><span class="brand-dot"></span><span class="brand-name">Polyfoam Council</span></div>
  <div class="title abs" style="left:132px;top:36px;font-weight:500;font-size:11px">Global Plastics Treaty</div>
  <div class="title abs" style="left:132px;top:50px;font-size:11px">Scientific Checks &amp; Balances</div>

  <div class="quote-mark" style="left:34px;top:78px">“</div>
  <div class="quote" style="left:32px;top:91px;width:76px">Some think science can provide definitive, complete and foolproof answers. But given the world’s complexity, different research modalities and replication limits, critical thinking must be embraced to develop policies that work.</div>
  <div class="quote-mark" style="left:86px;top:210px">”</div>

  <div class="check-row row-yes" style="top:86px;height:13px"><span class="ico"><svg width="8" height="8" viewBox="0 0 10 10"><path d="M1.5 5.2 4 7.6 8.6 2.4" fill="none" stroke="#fff" stroke-width="1.6"/></svg></span>The Body of Research on Plastic Is Extensive.</div>
  <div class="check-row row-ask" style="top:100px;height:13px"><span class="ico lbl" style="color:#fff;font-size:9px">?</span>Are All Plastics Toxic?</div>
  <div class="check-row row-ask" style="top:115px;height:21px"><span class="ico lbl" style="color:#fff;font-size:9px">?</span>Are NGO, Treaty Body or Industry Interpretations<br>Accurate or Inaccurate?</div>
  <div class="check-row row-no" style="top:137px;height:21px"><span class="ico"><svg width="8" height="8" viewBox="0 0 10 10"><path d="M2 2 8 8M8 2 2 8" stroke="#fff" stroke-width="1.6"/></svg></span>Is Data Transparency Evident For The Science<br>Supporting Policy Considerations?</div>
  <div class="check-row row-ask" style="top:159px;height:13px"><span class="ico lbl" style="color:#fff;font-size:9px">?</span>Problematic Plastics Are Classified Without Criteria</div>
  <div class="check-row row-yes" style="top:174px;height:21px"><span class="ico"><svg width="8" height="8" viewBox="0 0 10 10"><path d="M1.5 5.2 4 7.6 8.6 2.4" fill="none" stroke="#fff" stroke-width="1.6"/></svg></span>Is Scientific Information On Plastic Pollution Being<br>Used Out Of Context?</div>
  <div class="ask-pill">Know How To Ask The Right Questions</div>
  <div class="lbl abs" style="left:300px;top:194px;font-size:22px;color:var(--gold);font-weight:500">?</div>
</section>

<!-- ===== Slide 2 : NGO misuse of data ===== -->
<section class="slide" style="left:613px;top:36px">
  <div class="band" style="background:linear-gradient(180deg,var(--gold-warm),var(--gold))"></div>
  <div class="header" style="left:114px;width:200px;height:63px;background:var(--blue)"></div>
  <div class="abs" style="left:26px;top:26px;width:88px;height:63px;background:linear-gradient(90deg,var(--gold-warm),#9a8c4a)"></div>
  <div class="brand" style="left:42px;top:43px"><span class="brand-dot"></span><span class="brand-name">Polyfoam Council</span></div>
  <div class="title abs" style="left:127px;top:35px;font-weight:600;font-size:10.4px;letter-spacing:-.1px">NGO Misuse of Technical Data</div>
  <div class="abs small" style="left:127px;top:51px;width:180px;color:#fff">The definition of data misuse is <b>using any information in a way it’s not supposed to be used.</b> Terms of proper data use are usually specified in laws, industry standards, policies, and other agreements.</div>

  <div class="abs" role="img" aria-label="Waste coalition badge" style="left:54px;top:108px;width:32px;height:34px;background:#fff;border:1.5px solid var(--gold)"></div>
  <div class="abs" role="img" aria-label="First page of the cited journal study" style="left:40px;top:157px;width:59px;height:60px;background:linear-gradient(180deg,#ffffff,#eeeeee)"></div>

  <div class="abs small" style="left:127px;top:107px;width:188px"><b style="color:var(--gold);font-size:7px">False Claim:</b> “Polystyrene foam contains styrene, which has been linked to cancer, vision and hearing loss, impaired memory and concentration, and nervous system effects.”</div>
  <div class="abs tiny" style="left:127px;top:137px">Reference: Potential Toxicity of Polystyrene Micropolastics</div>
  <div class="abs small" style="left:127px;top:164px;width:190px"><b style="color:var(--blue);font-size:7px">Research Conclusions:</b> “The study confirmed that <b>PS particles were not toxic to human cells</b> at a dosage of ~500µg/mL and PS particles with diameters of 10-11 µm were not significantly cytotoxic”. Further, “It could be concluded that PS particles are not cytotoxic to HDFs and PBMCs in usual conditions but might cause damage in extreme, high concentrations.”</div>
  <div class="abs tiny" style="left:127px;top:217px;width:190px">Reference: Potential Toxicity of Polystyrene Microplastic Particles, Hanbit University, South Korea December 1, 2020</div>
</section>

<!-- ===== Slide 3 : Atmospheric studies ===== -->
<section class="slide" style="left:63px;top:319px">
  <div class="band" style="background:var(--blue)"></div>
  <div class="header" style="height:46px;background:var(--brown)"></div>
  <div class="title abs" style="left:36px;top:32px;font-weight:600;font-size:8.8px;letter-spacing:-.1px">Atmospheric Studies In 11 Cities Have Varying Results</div>
  <div class="abs" style="left:36px;top:45px;font-size:8px;line-height:10px;color:#fff">Does Microplastic Really Represent A Threat? A Review of<br>Atmospheric Contamination Sources &amp; Potential Impacts (2021)</div>

  <div class="quote-mark" style="left:33px;top:80px">“</div>
  <div class="quote" style="left:30px;top:93px;width:78px"><span style="padding-left:12px">In 11 studies in</span> specific locations (Europe, Asia, North America) airborne <b>polystyrene particles were found in only three cities.</b> The results represent three different test sample types and all three used varying air concentration calculations. Therefore, the <b>results are incompatible.</b></div>
  <div class="quote-mark" style="left:84px;top:206px">”</div>

  <div class="abs small" style="left:130px;top:88px;width:186px"><b style="color:var(--brown);font-size:7px">Thematic Hypothesis:</b> Atmospheric transport of microplastics is detrimental and is of great concern to the global community.</div>
  <div class="abs lbl" style="left:130px;top:111px;font-size:7px;color:var(--brown)">What’s Inside:</div>
  <ul class="abs small" style="left:138px;top:125px;width:178px;list-style:disc">
    <li style="margin-bottom:6px">There Are Three (3) Air Sampling Methodologies In This Developing Field of Study</li>
    <li style="margin-bottom:6px">No Standard Method Exists To Prepare Airborne Microplastic Test Samples</li>
    <li style="margin-bottom:6px">Visual Identification Methods Are Ineffective For Smaller Atmospheric Samples</li>
    <li>Studies Have Shown a Dominant Number of Airborne Microplastics are Fibers (≤95%).</li>
  </ul>
  <div class="abs small" style="left:130px;top:210px;width:186px"><b style="color:var(--brown);font-size:7px">Bottom Line:</b> There is a need to conduct comprehensive research on sources of atmospheric microplastics to aid in the initiation of effective control mechanisms and policy measures.</div>
</section>

<!-- ===== Slide 4 : Risk versus exposure ===== -->
<section class="slide" style="left:429px;top:319px">
  <div class="band" style="background:var(--brown)"></div>
  <div class="header" style="background:linear-gradient(90deg,#8f9618,var(--olive))"></div>
  <div class="title abs" style="left:39px;top:33px;font-weight:600;font-size:11px">Understanding Risk Versus Exposure</div>
  <div class="abs" style="left:39px;top:48px;font-size:7.2px;line-height:9.2px;color:#fff">Any substance can be poisonous. Chemicals of concern must be evaluated<br>within typical use parameters to evaluate its potential to present a hazard.</div>

  <div class="quote-mark" style="left:30px;top:74px">“</div>
  <div class="quote" style="left:30px;top:84px;width:80px;font-size:5.6px;line-height:6.8px"><span style="padding-left:10px">National Risk</span> Information Registry (NRIR) cautions that “NRIR values <b>cannot be validly used to accurately predict the incidence of human disease</b> or the type of effects that chemical exposures have on humans. This is due to the numerous uncertainties involved in risk assessment, including those associated with extrapolations from animal data to humans and from high experimental doses to lower environmental exposures.”</div>
  <div class="quote-mark" style="left:86px;top:204px">”</div>

  <svg class="abs" style="left:120px;top:80px" width="140" height="90" viewBox="0 0 140 90">
    <path d="M22 64 A48 48 0 0 1 116 64" fill="none" stroke="#9a9a9a" stroke-width=".6" stroke-dasharray="1.5 1.5"/>
    <circle cx="25" cy="68" r="1.3" fill="#555"/><circle cx="113" cy="68" r="1.3" fill="#555"/>
  </svg>
  <div class="risk-node" style="left:164px;top:119px;width:42px;height:42px;background:#f3f3f3;color:var(--ink);font-size:5.2px">
    <svg width="14" height="12" viewBox="0 0 14 12"><path d="M7 .5 13.5 11.5H.5Z" fill="#555"/><rect x="6.3" y="4" width="1.4" height="4" fill="#fff"/><rect x="6.3" y="9" width="1.4" height="1.4" fill="#fff"/></svg>
    <span style="margin-top:2px;text-align:center;line-height:5.6px">Risk of<br>Exposure</span></div>
  <div class="risk-node" style="left:137px;top:95px;width:28px;height:28px;background:var(--orange)"><svg width="8" height="8" viewBox="0 0 10 10"><circle cx="5" cy="5" r="4" fill="none" stroke="#fff"/><circle cx="5" cy="5" r="1.2" fill="#fff"/></svg>Toxicity</div>
  <div class="risk-node" style="left:171px;top:79px;width:28px;height:28px;background:var(--blue)"><svg width="8" height="8" viewBox="0 0 10 10"><circle cx="5" cy="5" r="4" fill="none" stroke="#fff"/><path d="M5 2.5V5H7" stroke="#fff" fill="none"/></svg>Duration</div>
  <div class="risk-node" style="left:205px;top:93px;width:28px;height:28px;background:var(--brown)"><svg width="8" height="8" viewBox="0 0 10 10"><circle cx="5" cy="5" r="4" fill="#fff"/><path d="M5 5 7 3" stroke="var(--brown)"/></svg>Frequency</div>
  <div class="risk-node" style="left:124px;top:130px;width:28px;height:28px;background:var(--olive)"><svg width="8" height="8" viewBox="0 0 10 10"><circle cx="5" cy="5" r="4" fill="#fff"/><path d="M2 8 8 2" stroke="var(--olive)"/></svg>Dose</div>
  <div class="risk-node" style="left:219px;top:130px;width:28px;height:28px;background:var(--gold-warm)"><svg width="8" height="8" viewBox="0 0 10 10"><circle cx="5" cy="4" r="2.5" fill="none" stroke="#fff"/><path d="M5 6.5V9" stroke="#fff"/></svg>Route of<br>Exposure</div>

  <div class="risk-box">Risk<br>Assessment<br>Involves<br>Reasonable<br>Assumptions<br>Under Different<br>Exposure<br>Scenarios To<br>Determine<br>Toxicity Levels</div>

  <div class="abs lbl" style="left:122px;top:174px;font-size:6.2px;color:var(--olive)">Is It Toxic? Scientific Ratings</div>
  <div class="abs" style="left:122px;top:184px;width:194px;font-size:5.1px;line-height:6.3px"><b style="font-size:6px">Carcinogens:</b> “no significant risk level” (“NSRL”) means that exposure to the amount of chemical in a product would result in no more than <b>one case of cancer out of every 100,000 individuals who were exposed to the chemical over a 70-year time period.</b></div>
  <div class="abs" style="left:122px;top:213px;width:194px;font-size:5.1px;line-height:6.3px"><b style="font-size:6px;color:var(--brown)">Reproductive Toxins:</b> Maximum allowable dose level (“MADL”) is the level at which a chemical would have no observable effect, even if an individual were exposed to 1,000 times that level.</div>
</section>

<!-- ===== Slide 5 : Expanded polystyrene emissions ===== -->
<section class="slide" style="left:796px;top:319px">
  <div class="header" style="left:3px;width:312px;height:41px;background:linear-gradient(90deg,#f3ecd6 0%,#dcc07a 18%,var(--gold-warm) 30%,var(--gold) 100%)"></div>
  <div class="abs" style="left:68px;top:26px;width:1px;height:41px;background:#fff;opacity:.8"></div>
  <div class="brand" style="left:24px;top:37px"><span class="brand-dot" style="width:20px;height:20px"></span><span class="brand-name" style="font-size:4.6px;line-height:5px;width:26px">Polyfoam Council</span></div>
  <div class="title abs" style="left:81px;top:33px;font-weight:600;font-size:10.8px;line-height:14px;letter-spacing:-.1px">Expanded Polystyrene Does Not Pose<br>A Human Health Threat</div>
  <div class="abs" style="left:81px;top:73px;font-size:8px;color:var(--ink)">Expanded Polystyrene Foam — Residual Styrene Emissions</div>

  <div class="table-head">
    <span class="abs" style="left:0;width:48px;top:15px;text-align:center">Exposure<br>Scenario</span>
    <span class="abs" style="left:47px;top:0;width:1px;height:42px;background:#fff"></span>
    <span class="abs" style="left:51px;top:6px;width:42px">Consumer Styrene Lifetime Average Daily Dose µg/day</span>
  </div>
  <div class="abs" style="left:73px;top:132px;width:.6px;height:97px;background:var(--ink-soft)"></div>
  <div class="trow" style="top:139px"><span class="k">Private<br>Office</span><span class="v" style="top:3px">0.05-0.79</span></div>
  <div class="trule" style="top:155px"></div>
  <div class="trow" style="top:160px"><span class="k">School<br>Classroom</span><span class="v" style="top:3px">0.03-0.48</span></div>
  <div class="trule" style="top:175px"></div>
  <div class="trow" style="top:180px"><span class="k">Home<br>Residence</span><span class="v" style="top:3px">0.48-7.33</span></div>
  <div class="trule" style="top:195px"></div>
  <div class="trow" style="top:201px"><span class="k">State Health<br>Agency Safe<br>Harbor<br>Styrene<br>NSRL</span><span class="v" style="top:9px">27</span></div>

  <svg class="abs" style="left:0;top:0" width="340" height="256" viewBox="0 0 340 256" font-family="Questrial, sans-serif" font-size="5.4" fill="#4a4a4a">
    <g text-anchor="end">
      <text x="157" y="113">30</text><text x="157" y="129">25</text><text x="157" y="144">20</text>
      <text x="157" y="159">15</text><text x="157" y="175">10</text><text x="157" y="190">5</text><text x="157" y="203">0</text>
    </g>
    <path d="M162 203 L290 236 M290 236 L305 196" stroke="#bdbdbd" stroke-width=".6" fill="none"/>
    <polygon points="185,102 193,99 303,110 296,114" fill="#b5bd32"/>
    <polygon points="296,114 303,110 301,193 294,197" fill="#7d8412"/>
    <polygon points="185,102 296,114 294,197 186,186" fill="var(--olive)"/>
    <polygon points="167,192 182,185 291,190 287,219 282,222 167,197" fill="var(--blue)"/>
    <polygon points="167,192 182,185 291,190 289,193 183,189" fill="#86afc9"/>
    <text x="203" y="138" fill="#fff" font-size="6" transform="rotate(6 203 138)">Styrene NSRL</text>
    <text x="203" y="145" fill="#fff" font-size="6" transform="rotate(6 203 145)">≤27µg/day IS NOT Harmful</text>
    <text x="254" y="207" fill="#fff" font-size="5.6" transform="rotate(10 254 207)">≤7.3µg/day</text>
    <text x="165" y="211">Office</text>
    <text x="213" y="222">School</text>
    <text x="274" y="236">Residence</text>
    <text x="306" y="195">NSRL</text>
    <text x="298" y="217">EPS</text>
  </svg>
</section>

</body>
</html>
```